Bed Company needs business card

Hello, we are a bed company that makes specialized magnets for beds. We are an alternative healing company. I need a modern and upscale business card. Please incorporate my logo for the card.

Accepted file formats are AI, EPS, and Press-Ready PDFS.

Please include all fonts or convert them to outlines regardless of file type.

If you are designing the card in Photoshop the file Must be 1200dpi.

I am open to anything for the business card.  I really like all of your designs and if you want to change the color of the logo, you can.  I will be making the final selection by Friday.  Thank You for all of your designs.  Feel Free to submit different color logos if you want.  

Reason: I will make a decision Final on Friday April 20th. 2012. Good Luck and Thank you all for the designs.

Target Market(s)

My target Market is people, who are looking for alternative healing.

Industry/Entity Type

Business

Requirements
Must have
• My logo must be incorporated. The front card must have

Name
Job Title

Address
Work
Cell
Fax
email
web

Just put in fake info for the card.

The back of the card. I want the logo on the back with color. I just want it to look modern and cool.

```html
<!DOCTYPE html>
<html lang="en">
<head>
<meta charset="utf-8">
<title>Restfield Business Card</title>
<link rel="stylesheet" href="https://fonts.googleapis.com/css2?family=Open+Sans:wght@400;600;700&display=swap">
<style>
  :root {
    --backdrop: #d0d0d0;
    --card: #ffffff;
    --band: #6aad45;
    --brand-dark: #1f7a2e;
    --ink: #444444;
    --on-band: #ffffff;
  }
  * { margin: 0; padding: 0; box-sizing: border-box; }
  html, body { width: 1200px; height: 900px; overflow: hidden; }
  body {
    background: var(--backdrop);
    font-family: "Open Sans", sans-serif;
    color: var(--ink);
    position: relative;
  }
  .card {
    position: absolute;
    top: 291px;
    width: 508px;
    height: 318px;
    background: var(--card);
  }
  .card--front { left: 65px; }
  .card--back { left: 618px; }
  .card__band {
    position: absolute;
    left: 0;
    width: 100%;
    height: 28px;
    background: var(--band);
  }
  .card__band--top { top: 0; }
  .card__band--bottom {
    bottom: 0;
    display: flex;
    align-items: center;
    justify-content: center;
    color: var(--on-band);
  }
  .event-line { font-size: 9.5px; letter-spacing: 0.1px; }
  .web-line { font-size: 13px; letter-spacing: 0.3px; }

  .identity {
    position: absolute;
    top: 68px;
    width: 100%;
    text-align: center;
  }
  .identity__name { font-size: 27px; font-weight: 400; line-height: 1.2; }
  .identity__title { font-size: 16px; color: var(--brand-dark); line-height: 1.2; }

  .contacts {
    position: absolute;
    top: 149px;
    left: 184px;
    font-size: 12.5px;
    line-height: 17.5px;
    border-collapse: collapse;
  }
  .contacts td { padding: 0; }
  .contacts .label { width: 32px; }
  .contacts .sep { width: 19px; }
  .email {
    position: absolute;
    top: 222px;
    width: 100%;
    text-align: center;
    font-size: 12.5px;
  }

  .brand {
    position: absolute;
    top: 116px;
    left: 0;
    width: 100%;
    display: flex;
    align-items: center;
    justify-content: center;
    gap: 12px;
  }
  .brand__mark {
    width: 34px;
    height: 34px;
    background: var(--brand-dark);
  }
  .brand__name {
    font-size: 32px;
    font-weight: 700;
    color: var(--band);
    letter-spacing: -0.5px;
  }
</style>
</head>
<body>
  <section class="card card--front">
    <div class="card__band card__band--top"></div>
    <div class="identity">
      <p class="identity__name">Daniel Morrow</p>
      <p class="identity__title">director</p>
    </div>
    <table class="contacts">
      <tr><td class="label">tel</td><td class="sep">:</td><td>(999) 999 999</td></tr>
      <tr><td class="label">cell</td><td class="sep">:</td><td>(999) 999 000</td></tr>
      <tr><td class="label">fax</td><td class="sep">:</td><td>(999) 000 000</td></tr>
    </table>
    <p class="email">office@restfieldcare.com</p>
    <div class="card__band card__band--bottom">
      <span class="event-line">June 5-8, 2012, Harborline Hall East, Lakeview IL, Booth 1473</span>
    </div>
  </section>

  <section class="card card--back">
    <div class="card__band card__band--top"></div>
    <div class="brand">
      <span class="brand__mark"></span>
      <span class="brand__name">Restfield</span>
    </div>
    <div class="card__band card__band--bottom">
      <span class="web-line">www.restfield-care.com</span>
    </div>
  </section>
</body>
</html>
```